Website for a financial survey consultancy

WHO WE ARE
We're a niche HR consultancy specialising in salary comparison surveys for the financial asset management industry. We position ourselves as a small, highly responsive organisation with a strong personal relationship with each of our 50+ blue-chip clients.

WHAT WE DO
Our business is 80% surveys (= products), 20% consultancy (= services). The surveys are a set of online products which clients interact with to find the information they are interested in.

WHAT WE WANT
We are completely revising our existing marketing website and need a new up-to-date look and feel for the site. We want you to design 2 web pages
- Home page
- Internal content page

More details below in Must Have Priorities.

REFERENCE SITES
- www.tallowmere.com - nice background image
- www.quimbelt.com - ignoring the animations
- www.palvastro.com
- www.dulmiko.com - clean, fresh, styly but prob not corporate enough
- www.orvettagrove.com - spacious, beautiful, slightly dated tho
- www.plinzer.co.uk - ignore the colours. Like the simplicity, larger font size (although want to stick with sans-serif fonts for main content)

DELIVERABLES
The final designs should be delivered as one or more PSD files with clearly named layers. All design elements and treatments should be separated out, for example use adjustment layers rather than applied (and subsequently irreversible) adjustments, strokes, shading, etc.

WHAT NEXT
I'll be monitoring the contest every day and can respond to questions fast. You can IM me on Skype or MSN.

Reason: Hi folks,

I am extending the deadline to this project as I am travelling this week and therefore will not be able to make a final decision until next Monday. I will try and provide further feedback over the course of this week but I am only going to be online occasionally so be prepared to wait a few days for a reply from me.

Thanks for all the designs so far.

Owen

Target Market(s)

In order of importance, most important first

1. Potential customers - UK & US financial industry HR professionals, short on time. Heard about us already, want to find out more about what we do, confirm relevance for their needs. Core goal - establish credibility: are we properly resourced, will we be around for years to come, are we *real*.

2. Existing customers - UK & US financial industry professionals, short on time, under pressure, want results quickly, minimum faff, expect high quality, slickly presented information. Primary action: login and use surveys.

3. Industry professionals/researchers - probably arriving through blog content, looking to browse and hoover information. Valuable for their ability to spread awareness of who we are amongst their peers.

Industry/Entity Type

Financial

Requirements
Must have
• GENERAL
Style cues - Corporate, professional, financial, stylish, slick, clean, spacious, light
Size - standard 960px grid

NAVIGATION
- [ Home | About us | Surveys | Consulting | Blog ]
- Sub-nav (roll-over dropdown) on About Us, Surveys & Consulting

ALL PAGES
- Site navigation
- Client login (on screen permanently or link to ajaxy in-page pop-up)
- Footer section
- Existing logo (attached)* - this is obviously an important reference point in the design, esp colour

HOME PAGE
- Communicate (link thru to?) survey/consulting split
- Large photo(s)/backdrop (2-3 interchangeable options ideally). Please consider what rights agreement will be necessary for any photos you include in your design.
- Possibly bigger more prominent version of logo
- Strap line/sentence - "Focussed data is the key to success"
- 3 recent blog posts (should look good with and without blog post images)
- Free downloadable PDF research report + supporting blurb

INTERNAL PAGE
- Page title
- Content - typical page will be less than one screenfull
- Level 1 sub-heading
- Level 2 sub-heading
- Bulleted list
- Content supporting image (any image will do - interested in placement, borders (if any), spacing, caption, etc)
- 'Do something' button

* Note: there is some internal debate about this logo at the moment. Some (me) are keen for it to change, some (not me!) are not. If you have an web page design idea/concept that requires an evolution of the logo, go ahead and evolve it. We can explore this further in the design process as necessary, but don't sweat it.
Nice to have
• Values to communicate
- Knowledgeable
- Professional
- Secure
- Personal
- Experienced
- Financial industry specific
- Accurate
- Reliable
Should not have
• - Search box
- Social media links, other than RSS feed button (discrete)

```html
<!DOCTYPE html>
<html lang="en">
<head>
<meta charset="utf-8">
<title>Halvren Consulting – Introduction</title>
<link rel="stylesheet" href="https://fonts.googleapis.com/css2?family=Mulish:ital,wght@0,400;0,700;0,800;1,400&display=swap">
<style>
:root{
  --page-bg:#eefbfc;
  --sheet:#ffffff;
  --brand-purple:#62006e;
  --arrow-purple:#5a0a7a;
  --nav-light:#1b9ae0;
  --nav-dark:#0d5f8e;
  --frame-navy:#14145a;
  --ink:#111111;
  --body-ink:#2a2a2a;
  --footer-bg:#fde07a;
  --footer-line:#6a6a3a;
}
*{box-sizing:border-box;margin:0;padding:0}
html,body{width:1200px;height:800px;overflow:hidden}
body{background:var(--page-bg);font-family:"Mulish",sans-serif;color:var(--ink);position:relative}
.sheet{position:absolute;left:170px;top:0;width:860px;height:800px;background:var(--sheet);box-shadow:0 0 10px rgba(0,0,0,.25)}
.brand-name{position:absolute;left:246px;top:40px;font-size:40px;font-weight:800;line-height:50px;color:var(--brand-purple)}
.login{position:absolute;left:851px;top:27px;width:115px;height:29px;border:1px solid #333;background:#fff;font-size:11px;line-height:27px;text-align:center;color:#222;text-decoration:none}
.page-title{position:absolute;left:537px;top:170px;font-size:47px;font-weight:800;line-height:60px;display:flex;align-items:center}
.page-title svg{margin-right:6px}
.nav-band{position:absolute;left:0;top:234px;width:1200px;height:36px}
.nav-links{position:absolute;left:0;top:234px;width:1200px;height:36px;list-style:none}
.nav-links li{position:absolute;top:0;transform:translateX(-50%);line-height:36px;font-size:14px;font-weight:700;color:#fff}
.banner{position:absolute;left:199px;top:276px;width:797px;height:120px;border:4px solid var(--frame-navy);border-radius:9px;background:linear-gradient(90deg,#0aa6c7 0%,#49e0ee 45%,#22b9dc 70%,#0a6fb0 100%)}
.content{position:absolute;left:199px;top:402px;width:797px;height:345px;border:4px solid var(--frame-navy);border-radius:11px;background:linear-gradient(180deg,#cfcfcf 0%,#ececec 45%,#ffffff 100%);padding:13px 10px 0 12px}
.content h1{font-size:21px;font-weight:800;line-height:26px}
.content h2{font-size:19px;font-weight:400;font-style:italic;line-height:24px}
.content p{font-size:13.1px;line-height:16.7px;color:var(--body-ink);margin-top:15px;letter-spacing:-.1px}
.question-list{list-style:none;font-size:13.1px;line-height:16.7px;color:var(--body-ink);margin-top:16px;letter-spacing:-.1px}
.btn-submit{position:absolute;left:13px;top:293px;width:60px;height:24px;border-radius:4px;background:linear-gradient(180deg,#555 0%,#111 55%,#000 100%);color:#fff;font-family:inherit;font-size:10px;border:1px solid #000;box-shadow:0 2px 2px rgba(0,0,0,.35)}
.footer{position:absolute;left:181px;top:755px;width:838px;height:50px;background:var(--footer-bg);border:1px solid var(--footer-line);text-align:center;font-size:14px;line-height:16px;padding-top:8px;color:#222}
</style>
</head>
<body>
<div class="sheet"></div>

<header>
  <span class="brand-name">Halvren</span>
  <a class="login" href="#">Login or Register</a>
  <div class="page-title">
    <svg width="36" height="36" viewBox="0 0 36 36" aria-hidden="true"><polygon points="2,3 34,18 2,33" fill="var(--arrow-purple)"/></svg>
    Introduction
  </div>
</header>

<nav>
  <svg class="nav-band" viewBox="0 234 1200 36" width="1200" height="36" aria-hidden="true">
    <polygon points="0,234 1200,234 1165,270 35,270" fill="var(--nav-light)"/>
    <polygon points="205,234 330,234 368,270 168,270" fill="var(--nav-dark)"/>
    <polygon points="500,234 665,234 700,270 535,270" fill="var(--nav-dark)"/>
    <polygon points="830,234 995,234 1032,270 868,270" fill="var(--nav-dark)"/>
  </svg>
  <ul class="nav-links">
    <li style="left:266px">Home</li>
    <li style="left:433px">About Us</li>
    <li style="left:596px">Surveys</li>
    <li style="left:767px">Consulting</li>
    <li style="left:930px">Blog</li>
  </ul>
</nav>

<div class="banner" role="img" aria-label="Silhouettes of business people standing before a glowing world map"></div>

<main class="content">
  <h1>Who are the good people at Halvren?</h1>
  <h2>Meet the team</h2>
  <p>Halvren Consulting is at the forefront in developing and implementing innovative approaches to the remuneration issues facing senior management in financial services.&nbsp; We conduct both regular and ad hoc research into remuneration and reward issues. The surveys have been designed, in close consultation with leading firms, to provide you with vital sector-specific information and data to help your firm answer these key questions:</p>
  <ul class="question-list">
    <li>Are we really performance driven?</li>
    <li>Are we getting value for money from our remuneration spend?</li>
    <li>Should we pay commissions to sales people?</li>
    <li>What is the most effective balance between short and long term remuneration?</li>
    <li>What are other firms doing on remuneration to get a competitive edge?</li>
  </ul>
  <p>For information please click on the button below to download the .pdf survey brochure.</p>
  <button class="btn-submit" type="button">Submit</button>
</main>

<footer class="footer">
  Halvren Consulting Ltd ► 14 Marlowe Court ► London EC2X 9QP<br>
  +44 (0)20 7946 0132 ► info@halvrenconsulting.com
</footer>
</body>
</html>
```